Communications Contractor Business Card Design

I would like a new business card for a new Communications company in Australia. Subcontracting and specialising in cabling, data, phone, antennas, pay tv ,modems, audio visual fibre optics etc. I am open to colour and design concepts but would like a modern clean look that stands out.

Industry/Entity Type

Tv

Contact Information for Business Card

kestrel communications pty ltd, Doug Pemberton, PO BOX 657 Marlow Flats QLD 4873 kestrel4me@maildrop-example.com Australia. ph 0437196084. Director/Technician. services- Cabling,data,phone,antennas,audio visual,home theatre, fibre optics.

```html
<!DOCTYPE html>
<html lang="en">
<head>
<meta charset="utf-8">
<title>Kestrel Communications – Business Card</title>
<link href="https://fonts.googleapis.com/css2?family=Questrial&family=Exo+2:wght@400;600&display=swap" rel="stylesheet">
<style>
  :root {
    --page-bg: #e6e6e6;
    --panel-dark: #333333;
    --accent-blue: #1ea7e1;
    --ink: #3a3a3a;
    --on-dark: #ffffff;
    --on-dark-soft: #d9d9d9;
  }
  * { box-sizing: border-box; margin: 0; padding: 0; }
  html, body {
    width: 1200px; height: 1018px; overflow: hidden;
    background: var(--page-bg);
  }
  .canvas { position: relative; width: 1200px; height: 1018px; }

  .card {
    position: absolute; width: 620px; height: 354px; overflow: hidden;
    box-shadow: 0 6px 18px rgba(0,0,0,0.18);
  }
  .card--front { left: 290px; top: 100px; }
  .card--back  { left: 290px; top: 560px; }
  .card__art { position: absolute; inset: 0; }

  .brand { position: absolute; color: var(--ink); font-family: "Questrial", sans-serif; font-weight: 400; }
  .brand__name { display: flex; align-items: center; gap: 10px; font-size: 62px; line-height: 1; letter-spacing: 0.5px; }
  .brand__dot { width: 14px; height: 14px; border-radius: 50%; background: var(--accent-blue); margin-top: 12px; }
  .brand__tagline { font-size: 17px; margin-top: 4px; margin-left: 2px; color: var(--ink); }
  .card--front .brand { left: 36px; top: 62px; }
  .card--back .brand { left: 70px; top: 122px; }

  .contact {
    position: absolute; right: 34px; top: 108px; width: 270px;
    font-family: "Exo 2", sans-serif; color: var(--on-dark); text-align: right;
  }
  .contact__rule { height: 1px; background: var(--on-dark); margin-bottom: 12px; }
  .contact__name { font-size: 22px; font-weight: 600; letter-spacing: 1px; line-height: 1.1; text-transform: uppercase; }
  .contact__role { font-size: 13px; letter-spacing: 1.5px; color: var(--on-dark-soft); margin-top: 2px; text-transform: uppercase; }
  .contact__list { list-style: none; margin-top: 22px; }
  .contact__item {
    display: flex; justify-content: flex-end; align-items: center; gap: 8px;
    font-size: 11px; letter-spacing: 0.4px; height: 25px; color: var(--on-dark-soft);
    white-space: nowrap;
  }
  .contact__icon { width: 17px; height: 17px; flex: none; }

  .web-strip {
    position: absolute; right: 26px; top: 36px; width: 30px; height: 282px;
    background: var(--on-dark); display: flex; align-items: center; justify-content: center;
  }
  .web-strip__text {
    transform: rotate(-90deg); white-space: nowrap;
    font-family: "Exo 2", sans-serif; font-size: 13px; letter-spacing: 1px; color: var(--ink);
  }
</style>
</head>
<body>
<main class="canvas">

  <section class="card card--front" aria-label="Business card front">
    <svg class="card__art" viewBox="0 0 620 354" width="620" height="354" aria-hidden="true">
      <defs>
        <linearGradient id="lightFace" x1="0" y1="0" x2="1" y2="1">
          <stop offset="0" stop-color="#ffffff"/>
          <stop offset="1" stop-color="#e2e2e2"/>
        </linearGradient>
      </defs>
      <rect width="620" height="354" fill="url(#lightFace)"/>
      <path d="M620 0 H427 A177 177 0 0 0 427 354 H620 Z" fill="var(--panel-dark)"/>
      <path d="M363 2 A186 186 0 0 0 247 225" fill="none" stroke="var(--accent-blue)" stroke-width="5"/>
    </svg>

    <div class="brand">
      <div class="brand__name">kestrel<span class="brand__dot"></span></div>
      <div class="brand__tagline">Communications Pty Ltd</div>
    </div>

    <div class="contact">
      <div class="contact__rule"></div>
      <div class="contact__name">Doug Pemberton</div>
      <div class="contact__role">Director / Technician</div>
      <ul class="contact__list">
        <li class="contact__item">0437196084
          <svg class="contact__icon" viewBox="0 0 20 20"><circle cx="10" cy="10" r="9" fill="none" stroke="#fff" stroke-width="1.4"/><path d="M7 5.5 L8.6 7.6 L7.6 8.8 Q8.8 11.4 11.2 12.4 L12.4 11.4 L14.5 13 L13.4 14.6 Q8.6 14.2 5.6 7 Z" fill="#fff"/></svg>
        </li>
        <li class="contact__item">0437 196 084
          <svg class="contact__icon" viewBox="0 0 20 20"><circle cx="10" cy="10" r="9" fill="none" stroke="#fff" stroke-width="1.4"/><rect x="7" y="5" width="6" height="10" rx="1" fill="none" stroke="#fff" stroke-width="1.3"/><circle cx="10" cy="13" r="0.8" fill="#fff"/></svg>
        </li>
        <li class="contact__item">kestrel4me@maildrop-example.com
          <svg class="contact__icon" viewBox="0 0 20 20"><circle cx="10" cy="10" r="9" fill="none" stroke="#fff" stroke-width="1.4"/><rect x="5.5" y="7" width="9" height="6.5" fill="none" stroke="#fff" stroke-width="1.2"/><path d="M5.5 7 L10 10.6 L14.5 7" fill="none" stroke="#fff" stroke-width="1.2"/></svg>
        </li>
        <li class="contact__item">www.kestrelcomms-example.com
          <svg class="contact__icon" viewBox="0 0 20 20"><circle cx="10" cy="10" r="9" fill="none" stroke="#fff" stroke-width="1.4"/><circle cx="10" cy="10" r="5" fill="none" stroke="#fff" stroke-width="1.1"/><ellipse cx="10" cy="10" rx="2.2" ry="5" fill="none" stroke="#fff" stroke-width="1"/><path d="M5 10 H15" stroke="#fff" stroke-width="1"/></svg>
        </li>
        <li class="contact__item">PO BOX 657 Marlow Flats QLD 4873
          <svg class="contact__icon" viewBox="0 0 20 20"><circle cx="10" cy="10" r="9" fill="none" stroke="#fff" stroke-width="1.4"/><path d="M10 15.5 Q6 11 6 8.5 A4 4 0 0 1 14 8.5 Q14 11 10 15.5 Z" fill="#fff"/><circle cx="10" cy="8.5" r="1.5" fill="var(--panel-dark)"/></svg>
        </li>
      </ul>
    </div>
  </section>

  <section class="card card--back" aria-label="Business card back">
    <svg class="card__art" viewBox="0 0 620 354" width="620" height="354" aria-hidden="true">
      <defs>
        <linearGradient id="lightFaceBack" x1="0" y1="0" x2="1" y2="1">
          <stop offset="0" stop-color="#ffffff"/>
          <stop offset="1" stop-color="#e2e2e2"/>
        </linearGradient>
      </defs>
      <rect width="620" height="354" fill="var(--panel-dark)"/>
      <path d="M0 0 H310 A160 160 0 0 1 470 160 V194 A160 160 0 0 1 310 354 H0 Z" fill="url(#lightFaceBack)"/>
    </svg>

    <div class="brand">
      <div class="brand__name">kestrel<span class="brand__dot"></span></div>
      <div class="brand__tagline">Communications Pty Ltd</div>
    </div>

    <div class="web-strip"><span class="web-strip__text">www.kestrelcomms-example.com</span></div>
  </section>

</main>
</body>
</html>
```